Need some visual "dash" to a dashboard UI design

Have a project that needs a little visual "zip". Attached are some screenshots of the current design. Will need source files of design work, Photoshop preferred, but Illustrator or other source will be acceptable. Please confirm before starting the work.

Here is a working prototype:
https://pm47rq.velnoria.com/#g=1&p=scenario_1_-_dashboard_view

Work has been done to get the UI elements in place, but need a little visual improvement to make it really "pop" ...while retaining its usability.

Primarily need some visual design done for the left column 5 elements revealing values for tech in and tech out between 0 and 20. Auth OT values are 0min, 30min, 60min, 90min, 120min, and "over 2 hours". Avail Reserve Capacity will be 0% through 10%. And Supply Delta can range from -10,000 to +10,000

Some design for the charts on the right would be great. Just trying to establish a visual language to apply to these values.

Please use colors from the approved palette with hex values (plus black and white):

Primary
Orange ff7200
Orange Highlight fcb314
Blue 067ab4
Blue Highlight 3aa5dc

Secondary
Lime b6bf00
Lime Highlight dbd810
Green 6ebb1f
Green Highlight c4d82d
Burgundy b30a3c
Burgundy Highlight da3872
Purple 81017e
Purple Highlight b8509e
Dark Blue 0c2577
Dark Blue Highlight 020bb3

Accent
Ochre eaab00
Magenta ff0066
Royal Blue 000066
Yellow ffef00
Teal 00c7b2
Dusty Blue 96b1d0
Light Blue bcc9d6
Mint Green 99ffcc
Gold ff9900
Taupe cccc66
Warm Gray cccc99

Industry/Entity Type

Work

Number of Pages Required

2 page

Font styles to use
Sans Serif

Requirements
Must have
• Must conform to the overall page layout described in the design doc attached. Must conform to the corporate color palette attached in the description.
• sorry, forgot to mention font: must use Verdana
• Verdana Font Family
• Verdana Regular
• Verdana Italic
• Verdana Bold
• Verdana Bold Italic

```html
<!DOCTYPE html>
<html lang="en">
<head>
<meta charset="utf-8">
<title>Verge – Capacity Planning Dashboard</title>
<link rel="stylesheet" href="https://fonts.googleapis.com/css2?family=Lato:wght@400;700;900&display=swap">
<style>
:root{
  --top-blue:#0d4fa6;
  --sub-blue:#0a3c85;
  --brand-blue:#0b56b0;
  --title-blue:#1a5ba8;
  --page:#e6e8eb;
  --white:#ffffff;
  --ink:#2b2b2b;
  --muted:#6b7480;
  --line:#c9d3de;
  --date-bar:#8c97a4;
  --open:#1f9a3c;
  --closed:#d0202a;
  --chart-orange:#ef8a26;
  --chart-blue:#4472c4;
  --chart-gray:#9a9a9a;
  --chart-yellow:#fcb314;
  --gold-btn:#f5b02a;
  --purple:#9b2f93;
  --teal:#2aa7c9;
  --focus-row:#dfe7f1;
  --footer:#222326;
}
*{box-sizing:border-box;margin:0;padding:0}
html,body{width:684px;height:1200px;overflow:hidden}
body{font-family:"Lato",sans-serif;background:var(--page);color:var(--ink);position:relative}

/* header */
.topbar{position:absolute;left:0;top:0;width:684px;height:28px;background:var(--top-blue)}
.brand{position:absolute;left:60px;top:7px;display:flex;align-items:center;gap:5px;color:var(--white);font-weight:700;font-size:10px}
.brand-dot{width:12px;height:12px;border-radius:50%;background:#5b8fd6}
.tab-active{position:absolute;left:126px;top:0;width:58px;height:28px;background:var(--sub-blue);color:var(--white);font-size:5px;text-align:center}
.tab-active svg{display:block;margin:5px auto 2px}
.tab-more{position:absolute;left:193px;top:0;width:18px;height:28px;color:var(--white);font-size:5px;text-align:center}
.tab-more svg{display:block;margin:6px auto 2px}
.subnav{position:absolute;left:0;top:28px;width:684px;height:10px;background:var(--sub-blue);color:var(--white);font-size:5px}
.subnav span{position:absolute;top:2px}
.subnav .current{border:1px solid var(--white);padding:0 6px;top:1px}

/* left column */
.actions{position:absolute;left:56px;top:78px;width:234px;height:720px;background:var(--white);box-shadow:0 0 0 1px #d3d8de;overflow:hidden}
.actions-head{height:32px;background:var(--brand-blue);color:var(--white);font-size:9px;font-weight:700;display:flex;align-items:center;padding-left:11px}
.select{position:absolute;left:64px;top:8px;width:142px;height:18px;background:var(--white);color:var(--ink);font-weight:400;font-size:7.5px;padding:4px 8px}
.select .caret{position:absolute;right:0;top:0;width:20px;height:18px;background:#c9ced4}
.select .caret:after{content:"";position:absolute;left:7px;top:8px;border:3px solid transparent;border-top-color:#555}
.tabs{display:flex;height:32px;font-size:8.5px}
.tabs div{flex:1;display:flex;align-items:center;justify-content:center}
.tabs .on{background:#e8f0fa;color:var(--brand-blue)}
.tabs .off{color:#555}
.datebar{position:relative;height:38px;background:var(--date-bar);color:var(--white);font-size:8.5px}
.datebar span{position:absolute;transform:translateX(-50%)}
.datebar .day{top:5px;font-weight:700}
.datebar .dt{top:24px;font-size:7px}
.datebar .rule{position:absolute;left:8px;right:8px;top:19px;height:1px;background:#b6bec8}
.datebar .mark{position:absolute;left:154px;top:18px;width:24px;height:3px;background:var(--chart-orange)}
.sites{position:relative}
.site{position:relative;border-bottom:1px solid var(--line);background:var(--white)}
.site.focus{background:var(--focus-row)}
.site-name{position:absolute;left:11px;top:12px;font-size:12px;font-weight:700;color:#333}
.badge{position:absolute;right:16px;top:12px;height:12px;padding:0 4px;font-size:7px;font-weight:700;color:var(--white);line-height:12px;letter-spacing:.3px}
.badge.open{background:var(--open)}
.badge.closed{background:var(--closed)}
.metrics{position:absolute;left:11px;top:35px;width:207px;height:27px}
.m-in{position:absolute;left:0;top:0;width:27px;height:27px;border:1px solid #c4c9cf;background:var(--white)}
.m-out{position:absolute;left:31px;top:0;width:22px;height:27px}
.m-in small,.m-out small{position:absolute;font-size:5.5px;color:#333;font-weight:700}
.m-ot{position:absolute;left:53px;top:1px;width:48px;height:24px;border:1px solid #c4c9cf;background:var(--white)}
.m-ot .lbl{position:absolute;left:19px;top:2px;font-size:6.5px;line-height:7px;color:#333}
.m-ot .bar{position:absolute;left:20px;right:3px;bottom:2px;height:2px;background:#c6cacf}
.m-ot .bar i{display:block;height:2px;background:var(--purple)}
.m-rsv{position:absolute;left:107px;top:-1px;width:48px;height:28px}
.m-rsv .lbl{position:absolute;left:0;top:0;font-size:6.5px;color:#333;white-space:nowrap}
.m-rsv .pct{position:absolute;left:21px;top:10px;font-size:6px;color:#333}
.m-rsv .bar{position:absolute;left:20px;width:26px;bottom:2px;height:2px;background:#c6cacf}
.m-rsv .bar i{display:block;height:2px;background:var(--teal)}
.m-delta{position:absolute;left:159px;top:0;width:48px;height:27px;background:var(--brand-blue);color:var(--white);font-size:6.5px;text-align:center}
.m-delta .t{display:block;margin-top:2px}
.m-delta .v{position:absolute;left:0;right:0;top:14px;font-size:7px}
.m-delta svg{position:absolute;left:8px;top:13px}
.buttons{position:absolute;left:32px;top:75px;display:flex;gap:6px}
.btn{height:24px;font-size:7.5px;font-weight:700;display:flex;align-items:center;justify-content:center;text-align:center;line-height:8.5px}
.btn.roll{width:68px;background:var(--gold-btn);color:var(--white)}
.btn.reserve{width:87px;border:1.5px solid #8a8f96;color:#666;background:transparent}
.scroll{position:absolute;right:0;top:180px;width:8px;height:540px;background:#f0f1f3;border-left:1px solid #d6dade}
.scroll .thumb{position:absolute;left:1px;top:150px;width:5px;height:26px;background:#c4c9cf}

/* filter panel */
.filters{position:absolute;left:315px;top:78px;width:313px;height:96px;background:var(--white)}
.f-label{position:absolute;font-size:8.5px;font-weight:700;color:#333}
.f-input{position:absolute;height:19px;border:1px solid #c4c9cf;font-size:7.5px;padding:5px 8px;color:#333;background:var(--white)}
.f-input .end{position:absolute;right:0;top:0;width:20px;height:17px;background:#e1e4e8}
.f-check{position:absolute;left:11px;top:52px;font-size:8px;color:#333;display:flex;align-items:center;gap:4px}
.f-check i{width:7px;height:7px;border:1px solid #777;display:block}

.page-title{position:absolute;left:314px;top:195px;font-size:17px;font-weight:900;color:var(--title-blue);letter-spacing:.3px}

.charts{position:absolute;left:315px;top:232px;width:313px;height:566px;background:var(--white)}
.card{position:absolute;width:151px;height:141px;background:var(--white)}
.card svg,.charts svg{position:absolute;left:0;top:0}

.footer{position:absolute;left:0;top:1154px;width:684px;height:46px;background:var(--footer);color:var(--white);font-size:7.5px}
.footer .copy{position:absolute;left:0;right:0;top:18px;text-align:center}
.footer .code{position:absolute;right:14px;top:17px;font-size:9px;font-weight:700}
svg text{font-family:"Lato",sans-serif}
</style>
</head>
<body>

<header class="topbar">
  <div class="brand"><span class="brand-dot"></span>VERGE</div>
  <div class="tab-active">
    <svg width="18" height="11" viewBox="0 0 18 11"><rect x="1" y="1" width="7" height="5" fill="#fcb314"/><rect x="10" y="4" width="7" height="5" fill="#fcb314"/><line x1="4" y1="6" x2="4" y2="10" stroke="#fff"/></svg>
    Capacity Planning
  </div>
  <div class="tab-more">
    <svg width="11" height="11" viewBox="0 0 11 11"><circle cx="5.5" cy="5.5" r="4.8" fill="none" stroke="#fff"/><circle cx="3.3" cy="5.5" r=".8" fill="#fff"/><circle cx="5.5" cy="5.5" r=".8" fill="#fff"/><circle cx="7.7" cy="5.5" r=".8" fill="#fff"/></svg>
    More
  </div>
</header>
<nav class="subnav">
  <span class="current" style="left:70px">Dashboard</span>
  <span style="left:145px">Lights</span>
  <span style="left:198px">Daily Plan</span>
  <span style="left:251px">Long Term Plan</span>
  <span style="left:316px">Schedule Recommendation</span>
  <span style="left:418px">Config</span>
</nav>

<section class="actions">
  <div class="actions-head">Actions for
    <div class="select">East Mounain Shores<span class="caret"></span></div>
  </div>
  <div class="tabs"><div class="on">Action Required (4)</div><div class="off">Review Required (9)</div></div>
  <div class="datebar">
    <span class="day" style="left:34px">Today</span>
    <span class="day" style="left:102px">Tomorrow</span>
    <span class="day" style="left:164px">+2</span>
    <span class="day" style="left:209px">+3</span>
    <div class="rule"></div><div class="mark"></div>
    <span class="dt" style="left:33px">03.12</span>
    <span class="dt" style="left:103px">03.13</span>
    <span class="dt" style="left:165px">03.14</span>
    <span class="dt" style="left:210px">03.15</span>
  </div>

  <div class="sites">
    <!-- site card template repeated -->
    <article class="site" style="height:77px">
      <h3 class="site-name">Hopkinsville_CB</h3><span class="badge open">OPEN</span>
      <div class="metrics">
        <div class="m-in"><svg width="27" height="27" viewBox="0 0 27 27"><circle cx="11" cy="8" r="3" fill="#6b7480"/><path d="M6 21v-6a5 5 0 0 1 10 0v6z" fill="#6b7480"/><path d="M3 15h6m-2-2 2 2-2 2" stroke="#333" fill="none"/></svg><small style="right:2px;top:1px">+5</small><small style="right:3px;bottom:0">IN</small></div>
        <div class="m-out"><svg width="22" height="20" viewBox="0 0 22 20"><circle cx="9" cy="5" r="3" fill="var(--brand-blue)"/><path d="M4 18v-6a5 5 0 0 1 10 0v6z" fill="var(--brand-blue)"/><path d="M13 13h6m-2-2 2 2-2 2" stroke="#fff" stroke-width="1.2" fill="none"/></svg><small style="left:3px;bottom:0">OUT</small></div>
        <div class="m-ot"><svg width="18" height="22" viewBox="0 0 18 22"><circle cx="9" cy="11" r="5" fill="none" stroke="var(--purple)" stroke-width="1.5"/><path d="M9 8v3h2" stroke="var(--purple)" fill="none"/></svg><span class="lbl">Auth OT<br>0 Min</span><span class="bar"><i style="width:0"></i></span></div>
        <div class="m-rsv"><span class="lbl">Avail RSV Cap</span><svg width="20" height="28" viewBox="0 0 20 28"><circle cx="7" cy="13" r="2.5" fill="var(--teal)"/><path d="M2 24v-4a5 5 0 0 1 10 0v4z" fill="var(--teal)"/><circle cx="13" cy="12" r="2.5" fill="var(--teal)"/><path d="M9 23v-4a5 5 0 0 1 9 0v4z" fill="var(--teal)"/></svg><span class="pct">0%</span><span class="bar"><i style="width:0"></i></span></div>
        <div class="m-delta"><span class="t">Supply Delta</span><svg width="12" height="8" viewBox="0 0 12 8"><path d="M6 0 12 8H0z" fill="#fff"/></svg><span class="v">&nbsp;&nbsp;&nbsp;&nbsp;+100</span></div>
      </div>
    </article>

    <article class="site" style="height:83px">
      <h3 class="site-name">Bowling_Green_CB</h3><span class="badge open">OPEN</span>
      <div class="metrics">
        <div class="m-in"><svg width="27" height="27" viewBox="0 0 27 27"><circle cx="11" cy="8" r="3" fill="#6b7480"/><path d="M6 21v-6a5 5 0 0 1 10 0v6z" fill="#6b7480"/><path d="M3 15h6m-2-2 2 2-2 2" stroke="#333" fill="none"/></svg><small style="right:2px;top:1px">+5</small><small style="right:3px;bottom:0">IN</small></div>
        <div class="m-out"><svg width="22" height="20" viewBox="0 0 22 20"><circle cx="9" cy="5" r="3" fill="var(--brand-blue)"/><path d="M4 18v-6a5 5 0 0 1 10 0v6z" fill="var(--brand-blue)"/><path d="M13 13h6m-2-2 2 2-2 2" stroke="#fff" stroke-width="1.2" fill="none"/></svg><small style="left:3px;bottom:0">OUT</small></div>
        <div class="m-ot"><svg width="18" height="22" viewBox="0 0 18 22"><circle cx="9" cy="11" r="5" fill="none" stroke="var(--purple)" stroke-width="1.5"/><path d="M9 8v3h2" stroke="var(--purple)" fill="none"/></svg><span class="lbl">Auth OT<br>0 Min</span><span class="bar"><i style="width:0"></i></span></div>
        <div class="m-rsv"><span class="lbl">Avail RSV Cap</span><svg width="20" height="28" viewBox="0 0 20 28"><circle cx="7" cy="13" r="2.5" fill="var(--teal)"/><path d="M2 24v-4a5 5 0 0 1 10 0v4z" fill="var(--teal)"/><circle cx="13" cy="12" r="2.5" fill="var(--teal)"/><path d="M9 23v-4a5 5 0 0 1 9 0v4z" fill="var(--teal)"/></svg><span class="pct">10%</span><span class="bar"><i style="width:30%"></i></span></div>
        <div class="m-delta"><span class="t">Supply Delta</span><svg width="12" height="8" viewBox="0 0 12 8"><path d="M6 0 12 8H0z" fill="#fff"/></svg><span class="v">&nbsp;&nbsp;&nbsp;&nbsp;0</span></div>
      </div>
    </article>

    <article class="site focus" style="height:117px">
      <h3 class="site-name">Memphis_North</h3><span class="badge closed">CLOSED</span>
      <div class="metrics">
        <div class="m-in"><svg width="27" height="27" viewBox="0 0 27 27"><circle cx="11" cy="8" r="3" fill="#6b7480"/><path d="M6 21v-6a5 5 0 0 1 10 0v6z" fill="#6b7480"/><path d="M3 15h6m-2-2 2 2-2 2" stroke="#333" fill="none"/></svg><small style="right:2px;top:1px">+5</small><small style="right:3px;bottom:0">IN</small></div>
        <div class="m-out"><svg width="22" height="20" viewBox="0 0 22 20"><circle cx="9" cy="5" r="3" fill="var(--brand-blue)"/><path d="M4 18v-6a5 5 0 0 1 10 0v6z" fill="var(--brand-blue)"/><path d="M13 13h6m-2-2 2 2-2 2" stroke="#fff" stroke-width="1.2" fill="none"/></svg><small style="left:3px;bottom:0">OUT</small></div>
        <div class="m-ot"><svg width="18" height="22" viewBox="0 0 18 22"><circle cx="9" cy="11" r="5" fill="none" stroke="var(--purple)" stroke-width="1.5"/><path d="M9 8v3h2" stroke="var(--purple)" fill="none"/></svg><span class="lbl">Auth OT<br>30 Min</span><span class="bar"><i style="width:20%"></i></span></div>
        <div class="m-rsv"><span class="lbl">Avail RSV Cap</span><svg width="20" height="28" viewBox="0 0 20 28"><circle cx="7" cy="13" r="2.5" fill="var(--teal)"/><path d="M2 24v-4a5 5 0 0 1 10 0v4z" fill="var(--teal)"/><circle cx="13" cy="12" r="2.5" fill="var(--teal)"/><path d="M9 23v-4a5 5 0 0 1 9 0v4z" fill="var(--teal)"/></svg><span class="pct">5%</span><span class="bar"><i style="width:15%"></i></span></div>
        <div class="m-delta"><span class="t">Supply Delta</span><svg width="12" height="8" viewBox="0 0 12 8"><path d="M6 0 12 8H0z" fill="#fff"/></svg><span class="v">&nbsp;&nbsp;&nbsp;&nbsp;-50</span></div>
      </div>
      <div class="buttons"><div class="btn roll">ROLL BACK</div><div class="btn reserve">UTILIZE RESERVE<br>CAPACITY</div></div>
    </article>

    <article class="site" style="height:81px">
      <h3 class="site-name">Memt_Jackson_CB</h3><span class="badge open">OPEN</span>
      <div class="metrics">
        <div class="m-in"><svg width="27" height="27" viewBox="0 0 27 27"><circle cx="11" cy="8" r="3" fill="#6b7480"/><path d="M6 21v-6a5 5 0 0 1 10 0v6z" fill="#6b7480"/><path d="M3 15h6m-2-2 2 2-2 2" stroke="#333" fill="none"/></svg><small style="right:2px;top:1px">+5</small><small style="right:3px;bottom:0">IN</small></div>
        <div class="m-out"><svg width="22" height="20" viewBox="0 0 22 20"><circle cx="9" cy="5" r="3" fill="var(--brand-blue)"/><path d="M4 18v-6a5 5 0 0 1 10 0v6z" fill="var(--brand-blue)"/><path d="M13 13h6m-2-2 2 2-2 2" stroke="#fff" stroke-width="1.2" fill="none"/></svg><small style="left:3px;bottom:0">OUT</small></div>
        <div class="m-ot"><svg width="18" height="22" viewBox="0 0 18 22"><circle cx="9" cy="11" r="5" fill="none" stroke="var(--purple)" stroke-width="1.5"/><path d="M9 8v3h2" stroke="var(--purple)" fill="none"/></svg><span class="lbl">Auth OT<br>0 Min</span><span class="bar"><i style="width:0"></i></span></div>
        <div class="m-rsv"><span class="lbl">Avail RSV Cap</span><svg width="20" height="28" viewBox="0 0 20 28"><circle cx="7" cy="13" r="2.5" fill="var(--teal)"/><path d="M2 24v-4a5 5 0 0 1 10 0v4z" fill="var(--teal)"/><circle cx="13" cy="12" r="2.5" fill="var(--teal)"/><path d="M9 23v-4a5 5 0 0 1 9 0v4z" fill="var(--teal)"/></svg><span class="pct">8%</span><span class="bar"><i style="width:25%"></i></span></div>
        <div class="m-delta"><span class="t">Supply Delta</span><svg width="12" height="8" viewBox="0 0 12 8"><path d="M6 0 12 8H0z" fill="#fff"/></svg><span class="v">&nbsp;&nbsp;&nbsp;&nbsp;+10,990</span></div>
      </div>
    </article>

    <article class="site" style="height:83px">
      <h3 class="site-name">Hopkinsville_CB</h3><span class="badge open">OPEN</span>
      <div class="metrics">
        <div class="m-in"><svg width="27" height="27" viewBox="0 0 27 27"><circle cx="11" cy="8" r="3" fill="#6b7480"/><path d="M6 21v-6a5 5 0 0 1 10 0v6z" fill="#6b7480"/><path d="M3 15h6m-2-2 2 2-2 2" stroke="#333" fill="none"/></svg><small style="right:2px;top:1px">+5</small><small style="right:3px;bottom:0">IN</small></div>
        <div class="m-out"><svg width="22" height="20" viewBox="0 0 22 20"><circle cx="9" cy="5" r="3" fill="var(--brand-blue)"/><path d="M4 18v-6a5 5 0 0 1 10 0v6z" fill="var(--brand-blue)"/><path d="M13 13h6m-2-2 2 2-2 2" stroke="#fff" stroke-width="1.2" fill="none"/></svg><small style="left:3px;bottom:0">OUT</small></div>
        <div class="m-ot"><svg width="18" height="22" viewBox="0 0 18 22"><circle cx="9" cy="11" r="5" fill="none" stroke="var(--purple)" stroke-width="1.5"/><path d="M9 8v3h2" stroke="var(--purple)" fill="none"/></svg><span class="lbl">Auth OT<br>0 Min</span><span class="bar"><i style="width:0"></i></span></div>
        <div class="m-rsv"><span class="lbl">Avail RSV Cap</span><svg width="20" height="28" viewBox="0 0 20 28"><circle cx="7" cy="13" r="2.5" fill="var(--teal)"/><path d="M2 24v-4a5 5 0 0 1 10 0v4z" fill="var(--teal)"/><circle cx="13" cy="12" r="2.5" fill="var(--teal)"/><path d="M9 23v-4a5 5 0 0 1 9 0v4z" fill="var(--teal)"/></svg><span class="pct">0%</span><span class="bar"><i style="width:0"></i></span></div>
        <div class="m-delta"><span class="t">Supply Delta</span><svg width="12" height="8" viewBox="0 0 12 8"><path d="M6 0 12 8H0z" fill="#fff"/></svg><span class="v">&nbsp;&nbsp;&nbsp;&nbsp;+100</span></div>
      </div>
    </article>

    <article class="site" style="height:81px">
      <h3 class="site-name">Bowling_Green_CB</h3><span class="badge closed">CLOSED</span>
      <div class="metrics">
        <div class="m-in"><svg width="27" height="27" viewBox="0 0 27 27"><circle cx="11" cy="8" r="3" fill="#6b7480"/><path d="M6 21v-6a5 5 0 0 1 10 0v6z" fill="#6b7480"/><path d="M3 15h6m-2-2 2 2-2 2" stroke="#333" fill="none"/></svg><small style="right:2px;top:1px">+5</small><small style="right:3px;bottom:0">IN</small></div>
        <div class="m-out"><svg width="22" height="20" viewBox="0 0 22 20"><circle cx="9" cy="5" r="3" fill="var(--brand-blue)"/><path d="M4 18v-6a5 5 0 0 1 10 0v6z" fill="var(--brand-blue)"/><path d="M13 13h6m-2-2 2 2-2 2" stroke="#fff" stroke-width="1.2" fill="none"/></svg><small style="left:3px;bottom:0">OUT</small></div>
        <div class="m-ot"><svg width="18" height="22" viewBox="0 0 18 22"><circle cx="9" cy="11" r="5" fill="none" stroke="var(--purple)" stroke-width="1.5"/><path d="M9 8v3h2" stroke="var(--purple)" fill="none"/></svg><span class="lbl">Auth OT<br>0 Min</span><span class="bar"><i style="width:0"></i></span></div>
        <div class="m-rsv"><span class="lbl">Avail RSV Cap</span><svg width="20" height="28" viewBox="0 0 20 28"><circle cx="7" cy="13" r="2.5" fill="var(--teal)"/><path d="M2 24v-4a5 5 0 0 1 10 0v4z" fill="var(--teal)"/><circle cx="13" cy="12" r="2.5" fill="var(--teal)"/><path d="M9 23v-4a5 5 0 0 1 9 0v4z" fill="var(--teal)"/></svg><span class="pct">10%</span><span class="bar"><i style="width:30%"></i></span></div>
        <div class="m-delta"><span class="t">Supply Delta</span><svg width="12" height="8" viewBox="0 0 12 8"><path d="M6 0 12 8H0z" fill="#fff"/></svg><span class="v">&nbsp;&nbsp;&nbsp;&nbsp;-1</span></div>
      </div>
    </article>

    <article class="site" style="height:96px;border-bottom:0">
      <h3 class="site-name">Memt_Jackson_CB</h3><span class="badge open">OPEN</span>
      <div class="metrics">
        <div class="m-in"><svg width="27" height="27" viewBox="0 0 27 27"><circle cx="11" cy="8" r="3" fill="#6b7480"/><path d="M6 21v-6a5 5 0 0 1 10 0v6z" fill="#6b7480"/><path d="M3 15h6m-2-2 2 2-2 2" stroke="#333" fill="none"/></svg><small style="right:2px;top:1px">+5</small><small style="right:3px;bottom:0">IN</small></div>
        <div class="m-out"><svg width="22" height="20" viewBox="0 0 22 20"><circle cx="9" cy="5" r="3" fill="var(--brand-blue)"/><path d="M4 18v-6a5 5 0 0 1 10 0v6z" fill="var(--brand-blue)"/><path d="M13 13h6m-2-2 2 2-2 2" stroke="#fff" stroke-width="1.2" fill="none"/></svg><small style="left:3px;bottom:0">OUT</small></div>
        <div class="m-ot"><svg width="18" height="22" viewBox="0 0 18 22"><circle cx="9" cy="11" r="5" fill="none" stroke="var(--purple)" stroke-width="1.5"/><path d="M9 8v3h2" stroke="var(--purple)" fill="none"/></svg><span class="lbl">Auth OT<br>0 Min</span><span class="bar"><i style="width:0"></i></span></div>
        <div class="m-rsv"><span class="lbl">Avail RSV Cap</span><svg width="20" height="28" viewBox="0 0 20 28"><circle cx="7" cy="13" r="2.5" fill="var(--teal)"/><path d="M2 24v-4a5 5 0 0 1 10 0v4z" fill="var(--teal)"/><circle cx="13" cy="12" r="2.5" fill="var(--teal)"/><path d="M9 23v-4a5 5 0 0 1 9 0v4z" fill="var(--teal)"/></svg><span class="pct">8%</span><span class="bar"><i style="width:25%"></i></span></div>
        <div class="m-delta"><span class="t">Supply Delta</span><svg width="12" height="8" viewBox="0 0 12 8"><path d="M6 0 12 8H0z" fill="#fff"/></svg><span class="v">&nbsp;&nbsp;&nbsp;&nbsp;+10,990</span></div>
      </div>
    </article>
  </div>
  <div class="scroll"><div class="thumb"></div></div>
</section>

<section class="filters">
  <span class="f-label" style="left:11px;top:9px">Previously viewed</span>
  <div class="f-input" style="left:11px;top:24px;width:141px">NSVL_PARIS_CB<span class="end"></span></div>
  <span class="f-label" style="left:162px;top:9px">Today</span>
  <div class="f-input" style="left:162px;top:24px;width:141px">03.12.2018<span class="end"></span></div>
  <div class="f-check"><i></i>Show date range</div>
  <div class="f-input" style="left:11px;top:66px;width:141px">NSVL_PARIS_CB<span class="end"></span></div>
  <svg style="position:absolute;left:171px;top:68px" width="40" height="14" viewBox="0 0 40 14">
    <rect x="1" y="6" width="2" height="7" fill="#fcb314"/><rect x="4" y="3" width="2" height="10" fill="#fcb314"/><rect x="7" y="5" width="2" height="8" fill="#fcb314"/><rect x="10" y="2" width="2" height="11" fill="#fcb314"/><line x1="0" y1="13.5" x2="14" y2="13.5" stroke="#fcb314"/>
    <line x1="21" y1="2" x2="21" y2="13" stroke="#555"/>
    <path d="M27 3l4-2 4 2 4-2v10l-4 2-4-2-4 2z" fill="#777"/>
  </svg>
</section>

<h1 class="page-title">DASHBOARD</h1>

<section class="charts">
  <svg width="313" height="566" viewBox="0 0 313 566">
    <g font-size="11.5" fill="#333" text-anchor="middle">
      <text x="156" y="32">Intakes vs Completions</text>
      <text x="156" y="212">Technician Breakdown</text>
      <text x="156" y="402">Tech Utilization</text>
    </g>

    <!-- intakes vs completions -->
    <rect x="17" y="44" width="280" height="140" fill="none" stroke="#e4e4e4"/>
    <g stroke="#e6e6e6" stroke-width=".6">
      <line x1="35" y1="54" x2="292" y2="54"/><line x1="35" y1="73" x2="292" y2="73"/><line x1="35" y1="91" x2="292" y2="91"/><line x1="35" y1="110" x2="292" y2="110"/><line x1="35" y1="129" x2="292" y2="129"/><line x1="35" y1="147" x2="292" y2="147"/>
    </g>
    <g font-size="4.5" fill="#555" text-anchor="end">
      <text x="31" y="56">250</text><text x="31" y="75">200</text><text x="31" y="93">150</text><text x="31" y="112">100</text><text x="31" y="131">50</text><text x="31" y="149">0</text>
    </g>
    <polyline fill="none" stroke="var(--chart-gray)" stroke-width="1" points="38,68.9 51.4,70.7 64.8,74.5 78.2,67 91.6,70.7 105,72.6 118.4,74.5 131.8,68.9 145.2,76.3 158.6,70.7 172,68.9 185.4,72.6 198.8,70.7 212.2,68.9 225.6,74.5 239,67 252.4,76.3 265.8,68.9 279.2,74.5 292.6,67"/>
    <polyline fill="none" stroke="var(--chart-yellow)" stroke-width="1" points="38,72.6 51.4,74.5 64.8,72.6 78.2,72.6 91.6,65.2 105,72.6 118.4,67 131.8,68.9 145.2,67 158.6,68.9 172,65.2 185.4,70.7 198.8,72.6"/>
    <polyline fill="none" stroke="var(--chart-blue)" stroke-width="1" points="38,107.9 51.4,108.7 64.8,109.1 78.2,104.2 91.6,107.9 105,106.1 118.4,107.9 131.8,106.1 145.2,107.9 158.6,106.8 172,106.8 185.4,109.1 198.8,106.8 212.2,103.1 225.6,109.1 239,108.3 252.4,106.8 265.8,103.1 279.2,103.8 292.6,106.1"/>
    <polyline fill="none" stroke="var(--chart-orange)" stroke-width="1" points="38,106.1 51.4,106.1 64.8,107.9 78.2,107.9 91.6,106.1 105,147 118.4,102.4 131.8,104.2 145.2,106.1 158.6,106.8 172,107.9 185.4,106.1 198.8,147"/>
    <g font-size="4" fill="#555" text-anchor="end">
      <text transform="translate(40,154) rotate(-50)">2/27/18</text><text transform="translate(53.4,154) rotate(-50)">2/28/18</text><text transform="translate(66.8,154) rotate(-50)">3/1/18</text><text transform="translate(80.2,154) rotate(-50)">3/2/18</text><text transform="translate(93.6,154) rotate(-50)">3/3/18</text><text transform="translate(107,154) rotate(-50)">3/4/18</text><text transform="translate(120.4,154) rotate(-50)">3/5/18</text><text transform="translate(133.8,154) rotate(-50)">3/6/18</text><text transform="translate(147.2,154) rotate(-50)">3/7/18</text><text transform="translate(160.6,154) rotate(-50)">3/8/18</text><text transform="translate(174,154) rotate(-50)">3/9/18</text><text transform="translate(187.4,154) rotate(-50)">3/10/18</text><text transform="translate(200.8,154) rotate(-50)">3/11/18</text><text transform="translate(214.2,154) rotate(-50)">3/12/18</text><text transform="translate(227.6,154) rotate(-50)">3/13/18</text><text transform="translate(241,154) rotate(-50)">3/14/18</text><text transform="translate(254.4,154) rotate(-50)">3/15/18</text><text transform="translate(267.8,154) rotate(-50)">3/16/18</text><text transform="translate(281.2,154) rotate(-50)">3/17/18</text><text transform="translate(294.6,154) rotate(-50)">3/18/18</text>
    </g>
    <g font-size="4.5" fill="#555">
      <line x1="52" y1="176" x2="62" y2="176" stroke="var(--chart-blue)"/><text x="64" y="177.5">Install Intakes</text>
      <line x1="105" y1="176" x2="115" y2="176" stroke="var(--chart-orange)"/><text x="117" y="177.5">Install Completions</text>
      <line x1="166" y1="176" x2="176" y2="176" stroke="var(--chart-gray)"/><text x="178" y="177.5">Repair Intakes</text>
      <line x1="216" y1="176" x2="226" y2="176" stroke="var(--chart-yellow)"/><text x="228" y="177.5">Repair Completions</text>
    </g>

    <!-- technician breakdown -->
    <rect x="17" y="224" width="276" height="144" fill="none" stroke="#e4e4e4"/>
    <g stroke="#e6e6e6" stroke-width=".6">
      <line x1="89" y1="234" x2="89" y2="354"/><line x1="110.8" y1="234" x2="110.8" y2="354"/><line x1="132.6" y1="234" x2="132.6" y2="354"/><line x1="154.4" y1="234" x2="154.4" y2="354"/><line x1="176.2" y1="234" x2="176.2" y2="354"/><line x1="198" y1="234" x2="198" y2="354"/><line x1="219.8" y1="234" x2="219.8" y2="354"/><line x1="241.6" y1="234" x2="241.6" y2="354"/><line x1="263.4" y1="234" x2="263.4" y2="354"/><line x1="285.2" y1="234" x2="285.2" y2="354"/>
    </g>
    <g font-size="5" fill="#444" text-anchor="end">
      <text x="83" y="245">Available Techs</text><text x="83" y="262">Techs on Proactive Load</text><text x="83" y="279">Loan Out</text><text x="83" y="297">Loan In</text><text x="83" y="314">Assigned to Load</text><text x="83" y="331">Unscheduled Techs</text><text x="83" y="348">Scheduled Techs</text>
    </g>
    <g fill="var(--chart-orange)">
      <rect x="89" y="239" width="25" height="5"/><rect x="89" y="256" width="49" height="5"/><rect x="89" y="273" width="10.9" height="5"/><rect x="89" y="308" width="96.9" height="5"/><rect x="89" y="325" width="21.8" height="5"/><rect x="89" y="342" width="181.9" height="5"/>
    </g>
    <g fill="var(--chart-blue)">
      <rect x="89" y="296" width="5.4" height="5"/><rect x="89" y="313" width="108.9" height="5"/><rect x="89" y="330" width="19.6" height="5"/><rect x="89" y="347" width="114.3" height="5"/>
    </g>
    <g font-size="4.8" fill="#444">
      <text x="117" y="244">23</text><text x="141" y="261">45</text><text x="103" y="278">10</text><text x="189" y="312">89</text><text x="114" y="329">20</text><text x="274" y="346">167</text>
    </g>
    <g font-size="5" fill="#444" text-anchor="middle">
      <text x="89" y="364">0</text><text x="110.8" y="364">20</text><text x="132.6" y="364">40</text><text x="154.4" y="364">60</text><text x="176.2" y="364">80</text><text x="198" y="364">100</text><text x="219.8" y="364">120</text><text x="241.6" y="364">140</text><text x="263.4" y="364">160</text><text x="285.2" y="364">180</text>
    </g>

    <!-- tech utilization -->
    <rect x="17" y="416" width="268" height="128" fill="none" stroke="#e4e4e4"/>
    <g stroke="#e6e6e6" stroke-width=".6">
      <line x1="89" y1="424" x2="89" y2="512"/><line x1="109.9" y1="424" x2="109.9" y2="512"/><line x1="130.8" y1="424" x2="130.8" y2="512"/><line x1="151.6" y1="424" x2="151.6" y2="512"/><line x1="172.5" y1="424" x2="172.5" y2="512"/><line x1="193.4" y1="424" x2="193.4" y2="512"/><line x1="214.3" y1="424" x2="214.3" y2="512"/><line x1="235.2" y1="424" x2="235.2" y2="512"/><line x1="256" y1="424" x2="256" y2="512"/><line x1="277" y1="424" x2="277" y2="512"/>
    </g>
    <g font-size="5" fill="#444" text-anchor="end">
      <text x="83" y="435">Available Techs</text><text x="83" y="457">Techs on Proactive work</text><text x="83" y="480">Techs on Load</text><text x="83" y="503">Activated Techs</text>
    </g>
    <g fill="var(--chart-orange)">
      <rect x="89" y="428" width="34.5" height="6"/><rect x="89" y="450" width="47" height="6"/><rect x="89" y="473" width="91.9" height="6"/><rect x="89" y="496" width="174.3" height="6"/>
    </g>
    <g fill="var(--chart-blue)">
      <rect x="89" y="479" width="104.4" height="6"/><rect x="89" y="502" width="104.4" height="6"/>
    </g>
    <g font-size="5" fill="#444" text-anchor="middle">
      <text x="89" y="522">0</text><text x="109.9" y="522">20</text><text x="130.8" y="522">40</text><text x="151.6" y="522">60</text><text x="172.5" y="522">80</text><text x="193.4" y="522">100</text><text x="214.3" y="522">120</text><text x="235.2" y="522">140</text><text x="256" y="522">160</text><text x="277" y="522">180</text>
    </g>
    <g font-size="4.5" fill="#555">
      <rect x="139" y="531" width="3.5" height="3.5" fill="var(--chart-orange)"/><text x="144" y="534.5">TFS</text>
      <rect x="156" y="531" width="3.5" height="3.5" fill="var(--chart-blue)"/><text x="161" y="534.5">IEFS</text>
    </g>
  </svg>
</section>

<!-- fill rate -->
<section class="card" style="left:315px;top:814px">
  <svg width="151" height="141" viewBox="0 0 151 141">
    <text x="11" y="22" font-size="11.5" font-weight="700" fill="#333">Fill Rate</text>
    <circle cx="94" cy="19" r="3" fill="none" stroke="var(--title-blue)" stroke-width="1.2"/><path d="M94 17.3v1.9h1.3" stroke="var(--title-blue)" fill="none" stroke-width=".8"/>
    <text x="100" y="21.5" font-size="7.5" fill="#333">03.12.2018</text>
    <circle cx="62" cy="83" r="40" fill="none" stroke="var(--chart-blue)" stroke-width="16"/>
    <circle cx="62" cy="83" r="40" fill="none" stroke="var(--chart-orange)" stroke-width="16" stroke-dasharray="78 251" transform="rotate(75 62 83)"/>
    <text x="62" y="90" font-size="17" font-weight="700" fill="#333" text-anchor="middle">112%</text>
    <path d="M113 128l4-5 4 5z" fill="var(--open)"/>
    <text x="123" y="129" font-size="7.5" fill="#333">5,1%</text>
  </svg>
</section>

<!-- installs / repairs -->
<section class="card" style="left:478px;top:814px">
  <svg width="151" height="141" viewBox="0 0 151 141">
    <circle cx="93" cy="17" r="3" fill="none" stroke="var(--title-blue)" stroke-width="1.2"/><path d="M93 15.3v1.9h1.3" stroke="var(--title-blue)" fill="none" stroke-width=".8"/>
    <text x="99" y="19.5" font-size="7.5" fill="#333">03.12.2018</text>
    <text x="38" y="42" font-size="10" fill="#333" text-anchor="middle">Installs</text>
    <text x="106" y="42" font-size="10" fill="#333" text-anchor="middle">Repairs</text>
    <g stroke="#ddd" stroke-width=".6">
      <line x1="24" y1="61" x2="64" y2="61"/><line x1="24" y1="77" x2="64" y2="77"/><line x1="24" y1="94" x2="64" y2="94"/><line x1="24" y1="110" x2="64" y2="110"/>
      <line x1="92" y1="61" x2="132" y2="61"/><line x1="92" y1="77" x2="132" y2="77"/><line x1="92" y1="94" x2="132" y2="94"/><line x1="92" y1="110" x2="132" y2="110"/>
    </g>
    <g font-size="7.5" fill="#333" text-anchor="end">
      <text x="21" y="64">120</text><text x="21" y="80">110</text><text x="21" y="97">100</text><text x="21" y="113">90</text>
      <text x="89" y="64">240</text><text x="89" y="80">220</text><text x="89" y="97">210</text><text x="89" y="113">200</text>
    </g>
    <rect x="34" y="94" width="5" height="16" fill="var(--chart-blue)"/><rect x="47" y="61" width="5" height="49" fill="var(--chart-orange)"/>
    <rect x="102" y="94" width="5" height="16" fill="var(--chart-blue)"/><rect x="115" y="61" width="5" height="49" fill="var(--chart-orange)"/>
    <rect x="13" y="123" width="6" height="6" fill="var(--chart-blue)"/><text x="25" y="129" font-size="7.5" fill="#333">Actual</text>
    <rect x="62" y="123" width="6" height="6" fill="var(--chart-orange)"/><text x="74" y="129" font-size="7.5" fill="#333">Projected</text>
  </svg>
</section>

<!-- duration -->
<section class="card" style="left:315px;top:968px">
  <svg width="151" height="141" viewBox="0 0 151 141">
    <text x="11" y="22" font-size="11.5" font-weight="700" fill="#333">Duration</text>
    <circle cx="94" cy="18" r="3" fill="none" stroke="var(--title-blue)" stroke-width="1.2"/><path d="M94 16.3v1.9h1.3" stroke="var(--title-blue)" fill="none" stroke-width=".8"/>
    <text x="100" y="20.5" font-size="7.5" fill="#333">03.12.2018</text>
    <g stroke="#ddd" stroke-width=".6">
      <line x1="30" y1="42" x2="140" y2="42"/><line x1="30" y1="62" x2="140" y2="62"/><line x1="30" y1="82" x2="140" y2="82"/><line x1="30" y1="102" x2="140" y2="102"/>
    </g>
    <g font-size="7.5" fill="#333" text-anchor="end">
      <text x="26" y="45">185</text><text x="26" y="65">150</text><text x="26" y="85">100</text><text x="26" y="105">50</text>
    </g>
    <rect x="40" y="42" width="5" height="60" fill="var(--chart-orange)"/><rect x="56" y="82" width="5" height="20" fill="var(--chart-blue)"/>
    <text x="10" y="116" font-size="6" fill="#333">Minutes</text>
    <rect x="13" y="124" width="6" height="6" fill="var(--chart-blue)"/><text x="25" y="130" font-size="7.5" fill="#333">Repair</text>
    <rect x="62" y="124" width="6" height="6" fill="var(--chart-orange)"/><text x="74" y="130" font-size="7.5" fill="#333">Install</text>
  </svg>
</section>

<!-- tech commit -->
<section class="card" style="left:478px;top:968px">
  <svg width="151" height="141" viewBox="0 0 151 141">
    <text x="11" y="22" font-size="11.5" font-weight="700" fill="#333">Tech Commit</text>
    <circle cx="93" cy="18" r="3" fill="none" stroke="var(--title-blue)" stroke-width="1.2"/><path d="M93 16.3v1.9h1.3" stroke="var(--title-blue)" fill="none" stroke-width=".8"/>
    <text x="99" y="20.5" font-size="7.5" fill="#333">03.12.2018</text>
    <g stroke="#ddd" stroke-width=".6">
      <line x1="30" y1="42" x2="140" y2="42"/><line x1="30" y1="62" x2="140" y2="62"/><line x1="30" y1="82" x2="140" y2="82"/><line x1="30" y1="102" x2="140" y2="102"/>
    </g>
    <g font-size="7.5" fill="#333" text-anchor="end">
      <text x="24" y="45">110</text><text x="24" y="65">105</text><text x="24" y="85">100</text><text x="24" y="105">95</text>
    </g>
    <rect x="40" y="42" width="5" height="60" fill="var(--chart-orange)"/><rect x="56" y="52" width="5" height="50" fill="var(--chart-blue)"/>
    <rect x="13" y="124" width="6" height="6" fill="var(--chart-blue)"/><text x="25" y="130" font-size="7.5" fill="#333">Actual</text>
    <rect x="62" y="124" width="6" height="6" fill="var(--chart-orange)"/><text x="74" y="130" font-size="7.5" fill="#333">Commit</text>
  </svg>
</section>

<footer class="footer">
  <p class="copy">Copyrights © 2018, Verge. All rights reserved.</p>
  <span class="code">C17</span>
</footer>

</body>
</html>
```